Varelto Stationary and Branding Documents

Corporate Identity Branding stationary needed for IT Recruiting Firm.

I already have a Logo, business cards and website. I need to get designs completed for the remaining corporate identity documents.

The documentation should use similar colors as my website and business card. The designs should modern and clean.

http://varelto-example.com/

Target Market(s)

Information Technology Industry

Industry/Entity Type

Information Technology

Colors
3377b5
0255a3
fbee3e
f78f20
f37122
33a6d7
000000
0592cd

Requirements
Must have
• Letter Head
• Folder Design
• PowerPoint Design
• Invoice
• Envelope
Nice to have
• Proposal
• Flyer
• Brochure
Should not have
• Logo
• Business Cards
• Website

```html
<!DOCTYPE html>
<html lang="en">
<head>
<meta charset="utf-8">
<title>Varelto Letterhead</title>
<link rel="stylesheet" href="https://fonts.googleapis.com/css2?family=Open+Sans:wght@400;600&display=swap">
<style>
  :root {
    --backdrop: #b6c4f2;
    --paper: #f7f8f9;
    --brand-blue: #0f5a9c;
    --brand-orange: #e67e22;
    --ink: #4a4a4a;
    --tile-1: #f8ebdc;
    --tile-2: #f5dfcb;
    --tile-3: #e7dac7;
  }
  * { margin: 0; padding: 0; box-sizing: border-box; }
  html, body { width: 1200px; height: 784px; overflow: hidden; }
  body {
    background: var(--backdrop);
    font-family: "Open Sans", sans-serif;
    position: relative;
  }
  .letterhead {
    position: absolute;
    left: 350px; top: 39px;
    width: 500px; height: 706px;
    background: var(--paper);
    box-shadow: 0 6px 18px rgba(40, 60, 140, 0.25);
    overflow: hidden;
  }
  .header-rule {
    position: absolute; left: 0; top: 10px;
    width: 318px; height: 5px;
    background: var(--brand-blue);
  }
  .brand-name {
    position: absolute; right: 34px; top: 14px;
    font-size: 30px; font-weight: 600;
    color: var(--brand-blue);
    letter-spacing: 1px;
    line-height: 1;
  }
  .header-accent {
    position: absolute; right: 0; top: 54px;
    width: 52px; height: 5px;
    background: var(--brand-orange);
  }
  .tiles { position: absolute; left: 0; top: 0; }
  .footer-contacts {
    position: absolute; left: 14px; bottom: 30px;
    display: flex; gap: 10px; align-items: center;
    font-size: 9px; color: var(--ink);
    white-space: nowrap;
  }
  .contact-item { display: flex; align-items: center; gap: 3px; }
  .contact-icon { width: 8px; height: 8px; }
  .footer-rules { position: absolute; left: 0; bottom: 0; }
  .web-tab {
    position: absolute; right: 0; bottom: 0;
    width: 140px; height: 30px;
    background: var(--brand-blue);
    clip-path: polygon(10% 0, 100% 0, 100% 100%, 0 100%);
    color: #fff; font-size: 10px; font-weight: 600;
    display: flex; align-items: center; justify-content: center;
    padding-left: 10px;
  }
</style>
</head>
<body>
  <main class="letterhead">
    <div class="header-rule"></div>
    <div class="brand-name">Varelto</div>
    <div class="header-accent"></div>

    <svg class="tiles" width="500" height="706" aria-hidden="true">
      <rect x="40" y="560" width="95" height="68" rx="14" fill="var(--tile-1)"/>
      <rect x="170" y="560" width="100" height="72" rx="14" fill="var(--tile-2)"/>
      <rect x="305" y="560" width="105" height="76" rx="14" fill="var(--tile-3)"/>
    </svg>

    <div class="footer-contacts">
      <span class="contact-item">
        <svg class="contact-icon" viewBox="0 0 10 10"><circle cx="5" cy="5" r="5" fill="var(--brand-blue)"/><circle cx="5" cy="4.2" r="1.6" fill="#fff"/></svg>
        Two Harbor Plaza 450 8th Street NE
      </span>
      <span class="contact-item">
        <svg class="contact-icon" viewBox="0 0 10 10"><circle cx="5" cy="5" r="5" fill="var(--brand-blue)"/><rect x="3" y="2.5" width="4" height="5" rx="1" fill="#fff"/></svg>
        8005550142
      </span>
      <span class="contact-item">
        <svg class="contact-icon" viewBox="0 0 10 10"><circle cx="5" cy="5" r="5" fill="var(--brand-blue)"/><rect x="2.5" y="3.2" width="5" height="3.6" fill="#fff"/></svg>
        info@varelto-example.com
      </span>
    </div>

    <svg class="footer-rules" width="500" height="26" aria-hidden="true">
      <rect x="0" y="6" width="120" height="4" fill="var(--brand-orange)"/>
      <rect x="124" y="6" width="104" height="4" fill="var(--brand-blue)"/>
      <rect x="232" y="6" width="130" height="4" fill="var(--brand-orange)"/>
      <rect x="0" y="18" width="370" height="5" fill="var(--brand-blue)"/>
    </svg>

    <div class="web-tab">www.varelto-example.com</div>
  </main>
</body>
</html>
```